New Stationary for our business

We are a gift business and would like to create a new corporate image with new stationary and design.

We would like a Classic Corporate look with a touch of Flair.

We would need:
Envelopes
Letter Head
Business Cards
With Comp Slips
Note Pads
Etc...

Our details are:

Basket Haven Pty Ltd
518 Pelling Street, Carrow Vale, Victoria, 3071
1800 742 918
www.baskethaven.com.au
sales@baskethaven.com.au

ABN: 62 804 319 775

Target Market(s)

Corporate Look

Industry/Entity Type

Marketing

Contact Information for Business Card

Basket Haven Pty Ltd
1800 742 918
518 Pelling Street
Carrow Vale 3071
Victoria Australia

Darren Pelloni - Managing Director
darren.pelloni@baskethaven.com.au
0417 586 902

Logo Text

Basket Haven - The Present Experts

Colors

Designer to choose colors to be used in the design.

Requirements
Must have
• Look and Feel upmarket and exclusive

```html
<!DOCTYPE html>
<html lang="en">
<head>
<meta charset="utf-8">
<title>Basket Haven – Presentation Folder</title>
<link href="https://fonts.googleapis.com/css2?family=Arimo:wght@400&display=swap" rel="stylesheet">
<style>
  :root {
    --backdrop: #d9d9db;
    --navy: #183766;
    --navy-deep: #142d55;
    --paper: #ffffff;
    --ink: #1f1f24;
    --muted: #8d8f94;
    --rule: #7d8aa3;
  }
  html, body {
    margin: 0;
    padding: 0;
    width: 1200px;
    height: 900px;
    overflow: hidden;
    background: var(--backdrop);
  }
  .folder-spread {
    position: absolute;
    left: 80px;
    top: 100px;
    width: 1040px;
    height: 700px;
    display: flex;
    box-shadow: 0 14px 40px rgba(0, 0, 0, 0.22);
  }
  .panel {
    position: relative;
    width: 520px;
    height: 700px;
    display: flex;
    flex-direction: column;
    background: var(--paper);
  }
  .panel + .panel {
    border-left: 1px solid rgba(0, 0, 0, 0.18);
  }
  .panel__colour-field {
    flex: 1;
    background: linear-gradient(180deg, var(--navy) 0%, var(--navy-deep) 100%);
  }
  .panel__band {
    position: relative;
    background: var(--paper);
  }
  .panel--back .panel__band {
    height: 150px;
  }
  .panel--front .panel__band {
    height: 118px;
  }

  /* Back cover: company details */
  .company-details {
    position: absolute;
    left: 0;
    right: 0;
    top: 42px;
    text-align: center;
    font-family: "Arimo", Arial, sans-serif;
    color: var(--ink);
  }
  .company-details p {
    margin: 0;
  }
  .company-details__name {
    font-size: 11px;
    letter-spacing: 1px;
    text-transform: uppercase;
    margin-bottom: 4px !important;
  }
  .company-details__address {
    font-size: 10px;
    margin-bottom: 5px !important;
  }
  .company-details__contact {
    display: flex;
    justify-content: center;
    align-items: center;
    gap: 14px;
    font-size: 10px;
    margin-bottom: 7px !important;
  }
  .company-details__divider {
    color: var(--ink);
  }
  .company-details__rule {
    display: inline-block;
    width: 26px;
    height: 1px;
    background: var(--rule);
  }
  .company-details__abn {
    font-size: 8px;
    color: var(--muted);
  }

  /* Front cover: name */
  .brand-name {
    position: absolute;
    right: 40px;
    top: 34px;
    display: flex;
    align-items: center;
    gap: 10px;
    font-family: "Arimo", Arial, sans-serif;
  }
  .brand-name__square {
    width: 14px;
    height: 14px;
    background: var(--navy);
  }
  .brand-name__text {
    margin: 0;
    font-size: 24px;
    color: var(--navy);
    letter-spacing: 0.3px;
    line-height: 1;
  }
  .brand-tagline {
    position: absolute;
    right: 40px;
    top: 68px;
    margin: 0;
    font-family: "Arimo", Arial, sans-serif;
    font-size: 10px;
    color: var(--muted);
    letter-spacing: 0.6px;
  }
</style>
</head>
<body>
  <main class="folder-spread">
    <section class="panel panel--back" aria-label="Back cover">
      <div class="panel__colour-field"></div>
      <div class="panel__band">
        <div class="company-details">
          <p class="company-details__name">Basket Haven Pty Ltd</p>
          <p class="company-details__address">518 Pelling Street, Carrow Vale, Victoria, 3071</p>
          <p class="company-details__contact">
            <span class="company-details__rule"></span>
            <span>www.baskethaven.com.au</span>
            <span class="company-details__divider">|</span>
            <span>1800 742 918</span>
            <span class="company-details__divider">|</span>
            <span>sales@baskethaven.com.au</span>
            <span class="company-details__rule"></span>
          </p>
          <p class="company-details__abn">ABN: 62 804 319 775</p>
        </div>
      </div>
    </section>

    <section class="panel panel--front" aria-label="Front cover">
      <div class="panel__colour-field"></div>
      <div class="panel__band">
        <div class="brand-name">
          <span class="brand-name__square"></span>
          <p class="brand-name__text">Basket Haven</p>
        </div>
        <p class="brand-tagline">The Present Experts</p>
      </div>
    </section>
  </main>
</body>
</html>
```